Product Packaging design for Vaporizer Battery box

We are looking for product packaging for a new line of Vaporizer Batteries. These batteries are all sold in bundle packs, and each battery has its own cardboard box. For example, the bundle packs are simply bagged up packs of 2, 3, 5, 10, 25, etc.

There are 4 different kinds of batteries that we need the packaging designed for. I have attached templates of the packaging for your reference. I would like the packaging to be a similar theme across all the batteries to keep things consistent.

More details about the 4 batteries can be found on our website at:
http://www.fernlockdistrib.example/product-category/vape_batteries/
Password: fernvisit

Packing Requirements

The packaging should have our company logo somewhere on it. I have attached a few different variations/orientations of our logo for you to choose between.

The name of the battery
Fernlock Goods 1300mAh Variable Voltage Large Capacity Battery
Fernlock Goods 400mAh Slim Variable Voltage Battery
Fernlock Goods 280mAh Slim Automatic Buttonless Battery
Fernlock Goods 350mAh TOV Slim Battery

Company website www.FernlockDistrib.example

For the Fernlock Goods 350mAh TOV Slim Battery, have the product packaging color scheme be Black base with Gold wording/trim. This battery only comes in black and gold, so the packaging will match.

Make sure to use the proper packaging template for the batteries. There are only two templates and pretty much the only difference is the size. They both fold up to be a rectangle package.

Industry/Entity Type

Product

Colors

Designer to choose colors to be used in the design.

Requirements
Must have
• Packing Requirements
• The packaging should have our company logo somewhere on it. I have attached a few different variations/orientations of our logo for you to choose between.
• The name of the battery
• Fernlock Goods 1300mAh Variable Voltage Large Capacity Battery
• Fernlock Goods 400mAh Slim Variable Voltage Battery
• Fernlock Goods 280mAh Slim Automatic Buttonless Battery
• Fernlock Goods 350mAh TOV Slim Battery
• Company website www.FernlockDistrib.example
• For the Fernlock Goods 350mAh TOV Slim Battery, have the product packaging color scheme be Black base with Gold wording/trim. This battery only comes in black and gold, so the packaging will match.
• Make sure to use the proper packaging template for the batteries. There are only two templates and pretty much the only difference is the size. They both fold up to be a rectangle package.

```html
<!DOCTYPE html>
<html lang="en">
<head>
<meta charset="utf-8">
<title>Fernlock Goods 1300mAh Battery Box – Dielines</title>
<link rel="stylesheet" href="https://fonts.googleapis.com/css2?family=Montserrat:wght@400;600&display=swap">
<style>
  :root {
    --bg-center: #f9a21c;
    --bg-mid: #f27417;
    --bg-edge: #b65814;
    --panel-dark: #232323;
    --panel-black: #050505;
    --gold: #f6c40f;
    --white: #ffffff;
    --trim-blue: #3a489c;
    --trim-gold: #f6c40f;
  }
  html, body {
    margin: 0;
    padding: 0;
    width: 1200px;
    height: 900px;
    overflow: hidden;
  }
  .canvas {
    width: 1200px;
    height: 900px;
    background: radial-gradient(ellipse at 50% 52%, var(--bg-center) 0%, var(--bg-mid) 45%, var(--bg-edge) 100%);
  }
  .canvas svg { display: block; width: 1200px; height: 900px; }
  .type { font-family: "Montserrat", sans-serif; }
  .brand-name { font-weight: 600; fill: var(--gold); letter-spacing: 3px; }
  .spec-copy { font-weight: 400; fill: var(--gold); font-size: 13px; letter-spacing: 0.5px; }
  .colour-option { font-weight: 400; fill: var(--white); font-size: 14px; }
  .flap-name { font-weight: 600; fill: var(--gold); font-size: 10px; letter-spacing: 1px; }
  .dieline-blue { color: var(--trim-blue); }
  .dieline-gold { color: var(--trim-gold); }
</style>
</head>
<body>
<div class="canvas">
<svg viewBox="0 0 1500 1125" xmlns="http://www.w3.org/2000/svg" class="type">
  <defs>
    <symbol id="battery-box" viewBox="0 0 470 1090" width="470" height="1090">
      <!-- top tuck flap -->
      <path class="tuck-flap" d="M116 0 h0 M116 30 a28 28 0 0 1 28 -28 h60 a28 28 0 0 1 28 28 V177 H116 Z" fill="var(--panel-dark)"/>
      <circle cx="158" cy="132" r="5" fill="var(--gold)"/>
      <text class="flap-name" x="175" y="136" text-anchor="middle" style="font-size:9px">FERNLOCK GOODS</text>
      <!-- top dust flaps -->
      <path class="dust-flap" d="M12 122 H96 L115 158 V177 H12 Z" fill="var(--panel-dark)"/>
      <path class="dust-flap" d="M252 122 H336 V165 L348 177 H232 V158 Z" fill="var(--panel-dark)"/>
      <!-- upper body (patterned area) -->
      <path class="body-upper" d="M0 186 L10 177 H465 V665 H0 Z" fill="var(--panel-dark)"/>
      <!-- lower body -->
      <path class="body-lower" d="M0 665 H465 V912 H0 V922 L0 912 Z" fill="var(--panel-black)"/>
      <!-- trim band with chevron -->
      <path class="trim-band" d="M0 665 H116 L174 705 L232 665 H465 V679 H232 L174 720 L116 679 H0 Z" fill="currentColor"/>
      <!-- bottom dust flaps -->
      <path class="dust-flap" d="M12 912 H115 L96 967 H12 Z" fill="var(--panel-black)"/>
      <path class="dust-flap" d="M232 912 H336 V967 H252 L232 940 Z" fill="var(--panel-black)"/>
      <!-- bottom tuck flap -->
      <path class="tuck-flap" d="M348 912 H465 V1060 a28 28 0 0 1 -28 28 H376 a28 28 0 0 1 -28 -28 Z" fill="var(--panel-black)"/>
      <circle cx="380" cy="995" r="5" fill="var(--gold)"/>
      <text class="flap-name" x="412" y="999" text-anchor="middle" style="font-size:8.5px">FERNLOCK</text>
      <text class="flap-name" x="406" y="1013" text-anchor="middle" style="font-size:8.5px">GOODS</text>

      <!-- front panel brand name -->
      <circle cx="175" cy="285" r="14" fill="var(--gold)"/>
      <text class="brand-name" transform="translate(186 490) rotate(90)" x="0" y="0" text-anchor="middle" style="font-size:30px">FERNLOCK GOODS</text>

      <!-- spec copy -->
      <text class="spec-copy" text-anchor="middle">
        <tspan x="174" y="753">1300mAh</tspan>
        <tspan x="174" y="769">VARIABLE</tspan>
        <tspan x="174" y="785">VOLTAGE</tspan>
        <tspan x="174" y="817">LARGE</tspan>
        <tspan x="174" y="833">CAPACITY</tspan>
        <tspan x="174" y="849">BATTERY</tspan>
      </text>

      <!-- colour options -->
      <g class="colour-options">
        <text class="colour-option" transform="translate(263 792) rotate(-90)">GREEN</text>
        <text class="colour-option" transform="translate(282 792) rotate(-90)">PURPLE</text>
        <text class="colour-option" transform="translate(301 792) rotate(-90)">STAINLESS</text>
        <text class="colour-option" transform="translate(321 792) rotate(-90)">TITANIUM</text>
        <rect x="252" y="800" width="13" height="13" fill="var(--white)"/>
        <rect x="271" y="800" width="13" height="13" fill="var(--white)"/>
        <rect x="290" y="800" width="13" height="13" fill="var(--white)"/>
        <rect x="310" y="800" width="13" height="13" fill="var(--white)"/>
        <text class="colour-option" transform="translate(263 868) rotate(-90)">BLACK</text>
        <text class="colour-option" transform="translate(282 868) rotate(-90)">WHITE</text>
        <text class="colour-option" transform="translate(301 868) rotate(-90)">RED</text>
        <text class="colour-option" transform="translate(321 868) rotate(-90)">BLUE</text>
        <rect x="252" y="876" width="13" height="13" fill="var(--white)"/>
        <rect x="271" y="876" width="13" height="13" fill="var(--white)"/>
        <rect x="290" y="876" width="13" height="13" fill="var(--white)"/>
        <rect x="310" y="876" width="13" height="13" fill="var(--white)"/>
      </g>

      <!-- compliance marks as plain shapes -->
      <g class="compliance-marks" fill="none" stroke="var(--white)" stroke-width="3">
        <circle cx="409" cy="728" r="13"/>
        <circle cx="409" cy="780" r="16"/>
        <circle cx="409" cy="831" r="13" fill="var(--white)"/>
        <rect x="394" y="857" width="30" height="30"/>
      </g>
    </symbol>
  </defs>

  <use href="#battery-box" class="dieline-blue" x="270" y="20" width="470" height="1090"/>
  <use href="#battery-box" class="dieline-gold" x="768" y="20" width="470" height="1090"/>
</svg>
</div>
</body>
</html>
```